A Speech Therapy Business needs to update their logo

I need an update to the font and color of my logo to look more appealing. I am looking to open a private practice as a Speech Language Pathologist that caters to adults and children. It needs to be sophisticated and friendly at the same time. I want to keep the silhouette in my logo as is, just update the font and color for "Brightpath".
Industry/Entity Type
Business
Contact Information for Business Card
I want the business card to have my logo, my name (Odile Varn, CCC-SLP, TSSLD) and that I am a Bilingual Speech Language Pathologist. Also, include my phone number, (718) 555-0193. Include my website, Brightpathslp.example, and email address, odilevarn@brightpathslp.example
Look and feel

```html
<!DOCTYPE html>
<html lang="en">
<head>
<meta charset="utf-8">
<title>Brightpath Business Card</title>
<link rel="stylesheet" href="https://fonts.googleapis.com/css2?family=Source+Sans+3:wght@400;600;700&display=swap">
<style>
  :root {
    --brand-purple: #7b5ea7;
    --ink: #1e1e1e;
    --muted: #5a5a5a;
    --rule: #9a9a9a;
    --paper: #ffffff;
    --stage: #e8e6ea;
    --silhouette: #1a1a1a;
  }
  * { margin: 0; padding: 0; box-sizing: border-box; }
  html, body {
    width: 1200px;
    height: 987px;
    overflow: hidden;
    background: var(--stage);
    font-family: "Source Sans 3", Arial, sans-serif;
  }
  .canvas { position: relative; width: 1200px; height: 987px; }

  .card {
    position: absolute;
    width: 615px;
    height: 352px;
    box-shadow: 0 2px 6px rgba(0,0,0,0.18);
  }
  .card--front { left: 293px; top: 130px; background: var(--paper); }
  .card--back  { left: 292px; top: 506px; background: var(--brand-purple); }

  .logo { position: absolute; left: 387px; top: 26px; width: 197px; }
  .logo__figures {
    display: block;
    width: 197px;
    height: 76px;
    background: linear-gradient(90deg, var(--silhouette), #3a3a3a);
    border-radius: 4px;
  }
  .logo__name {
    display: block;
    margin-top: 6px;
    font-size: 40px;
    font-weight: 400;
    line-height: 1;
    color: var(--brand-purple);
    text-align: center;
    letter-spacing: 0.5px;
  }

  .identity { position: absolute; left: 27px; top: 190px; width: 554px; }
  .identity__name {
    font-size: 22px;
    font-weight: 700;
    color: var(--brand-purple);
    line-height: 1.1;
  }
  .identity__credentials { font-size: 15px; font-weight: 600; }
  .identity__title {
    margin-top: 4px;
    font-size: 16px;
    color: var(--ink);
  }
  .identity__rule {
    margin-top: 12px;
    border: 0;
    border-top: 1px solid var(--rule);
  }

  .contacts { list-style: none; margin-top: 10px; }
  .contacts__item {
    display: flex;
    align-items: center;
    gap: 8px;
    height: 24px;
    font-size: 15.5px;
    color: var(--muted);
  }
  .contacts__icon { width: 13px; height: 13px; fill: var(--brand-purple); flex: none; }

  .back-figures {
    position: absolute;
    left: 352px; top: 205px;
    width: 226px; height: 92px;
    background: linear-gradient(90deg, var(--silhouette), #2e2a36);
    border-radius: 4px;
  }
  .back-url {
    position: absolute;
    left: 356px; top: 302px;
    font-size: 15.5px;
    color: #ffffff;
    letter-spacing: 1px;
    transform: rotate(5deg);
    transform-origin: left center;
  }
</style>
</head>
<body>
<main class="canvas">
  <section class="card card--front">
    <div class="logo">
      <span class="logo__figures" role="img" aria-label="Silhouette illustration of a line of adults and children holding hands, ending in a small heart"></span>
      <span class="logo__name">Brightpath</span>
    </div>

    <div class="identity">
      <h1 class="identity__name">Odile Varn, <span class="identity__credentials">CCC-SLP, TSSLD</span></h1>
      <p class="identity__title">Bilingual Speech Language Pathologist</p>
      <hr class="identity__rule">
      <ul class="contacts">
        <li class="contacts__item">
          <svg class="contacts__icon" viewBox="0 0 16 16" aria-hidden="true"><path d="M3.6 1.2l2.3 2.6-1.3 1.9c.9 2 2.6 3.7 4.6 4.6l1.9-1.3 2.6 2.3-1.2 2.2C7.1 14.9 1.1 8.9.9 3.6z"/></svg>
          (718) 555-0193
        </li>
        <li class="contacts__item">
          <svg class="contacts__icon" viewBox="0 0 16 16" aria-hidden="true"><path d="M1 3h14v10H1z M1 3l7 6 7-6" fill="var(--brand-purple)"/><path d="M1.5 3.5l6.5 5.5 6.5-5.5" fill="none" stroke="#fff" stroke-width="1.2"/></svg>
          odilevarn@brightpathslp.example
        </li>
        <li class="contacts__item">
          <svg class="contacts__icon" viewBox="0 0 16 16" aria-hidden="true"><circle cx="8" cy="8" r="7"/><path d="M1 8h14M8 1c-3 3.5-3 10.5 0 14M8 1c3 3.5 3 10.5 0 14" fill="none" stroke="#fff" stroke-width="1"/></svg>
          www.Brightpathslp.example
        </li>
      </ul>
    </div>
  </section>

  <section class="card card--back">
    <span class="back-figures" role="img" aria-label="Silhouette illustration of a line of adults and children holding hands, ending in a small heart"></span>
    <p class="back-url">www.Brightpathslp.example</p>
  </section>
</main>
</body>
</html>
```